Stonegate Towing Business Card

Towing
Accident towing
Mechanical breakdown
Insurance, salvage and recovery
4wd off road towing
Light & Heavy towing
7354 2618
24 hour business 7 days

Logo can be whole size on front

Industry/Entity Type

Towing/ transport

Contact Information for Business Card

The above

```html
<!DOCTYPE html>
<html lang="en">
<head>
<meta charset="utf-8">
<title>Stonegate Towing Business Card</title>
<link rel="stylesheet" href="https://fonts.googleapis.com/css2?family=Raleway:wght@500;800&display=swap">
<style>
  :root {
    --stage: #d6d6d6;
    --card: #222127;
    --card-tone: #2c2b31;
    --red: #e0242b;
    --white: #ffffff;
    --grey-name: #3a393f;
  }
  * { margin: 0; padding: 0; box-sizing: border-box; }
  html, body { width: 1200px; height: 856px; overflow: hidden; }
  body {
    background: var(--stage);
    font-family: "Raleway", "Helvetica Neue", Arial, sans-serif;
    display: flex;
    align-items: center;
    justify-content: center;
    gap: 40px;
  }
  .card {
    position: relative;
    width: 540px;
    height: 309px;
    background: var(--card);
    box-shadow: 0 14px 30px rgba(0,0,0,0.35);
    overflow: hidden;
  }
  .faint-name {
    position: absolute;
    left: 26px;
    top: 24px;
    font-weight: 800;
    font-size: 22px;
    color: var(--card-tone);
    letter-spacing: 0.5px;
  }
  .phone {
    position: absolute;
    right: 28px;
    top: 26px;
    display: flex;
    align-items: center;
    gap: 8px;
    color: var(--white);
    font-weight: 500;
    font-size: 15px;
    letter-spacing: 0.5px;
  }
  .phone svg { width: 16px; height: 16px; }
  .services {
    position: absolute;
    left: 28px;
    bottom: 26px;
    list-style: none;
    color: var(--white);
    font-weight: 500;
    font-size: 13px;
    line-height: 21px;
  }
  .services li { display: flex; align-items: center; gap: 10px; }
  .services li::before {
    content: "";
    width: 7px; height: 7px;
    border-radius: 50%;
    background: var(--red);
    flex: none;
  }
  .brand-name {
    position: absolute;
    right: 28px;
    top: 120px;
    width: 230px;
    text-align: right;
    font-weight: 800;
    font-size: 34px;
    line-height: 38px;
    color: var(--red);
  }
  .card-back { border-bottom: 4px solid var(--red); border-left: 4px solid var(--red); }
  .back-name {
    position: absolute;
    inset: 0;
    display: flex;
    align-items: center;
    justify-content: center;
    font-weight: 800;
    font-size: 46px;
    color: var(--grey-name);
    letter-spacing: 1px;
  }
</style>
</head>
<body>
  <section class="card card-front" aria-label="Card front">
    <div class="faint-name">Stonegate Towing</div>
    <div class="phone">
      <span>7354 2618</span>
      <svg viewBox="0 0 24 24" aria-hidden="true"><path fill="#e0242b" d="M6.6 10.8a15.1 15.1 0 0 0 6.6 6.6l2.2-2.2a1 1 0 0 1 1-.25 11.4 11.4 0 0 0 3.6.6 1 1 0 0 1 1 1V20a1 1 0 0 1-1 1A17 17 0 0 1 3 4a1 1 0 0 1 1-1h3.5a1 1 0 0 1 1 1c0 1.25.2 2.45.6 3.6a1 1 0 0 1-.25 1z"/></svg>
    </div>
    <ul class="services">
      <li>Towing</li>
      <li>Accident towing</li>
      <li>Mechanical breakdown</li>
      <li>Insurance, salvage and recovery</li>
      <li>4wd off road towing</li>
      <li>Light &amp; Heavy towing</li>
      <li>24/7 business</li>
    </ul>
    <div class="brand-name">Stonegate Towing</div>
  </section>
  <section class="card card-back" aria-label="Card back">
    <div class="back-name">Stonegate Towing</div>
  </section>
</body>
</html>
```